Vantoria Pocket Folder

Create a new pocket folder
An Overview / Background of the Business & Services
We would like a new folder to use when making formal presentations
* The Target Market / Audience you are trying to reach
The target audience are commercial businesses that we are selling group insurance products to
* Design Specifics; any preferences or ideas for Style, Colour, Imagery, etc
We wanted to use the Houston, Texas skyline and create something that was simple, yet modern.
* Do you have an existing website or Facebook page were designers can learn more about your company?
Yes, http://www.vantoriagroup-example.com and we are on Linked-In.
Project Deadline Extended Reason: We have many people who have to agree. We need to get an answer on the form of the ready art we will receive when we select a designer .Thank you. Added Thursday, April 27, 2017

```html
<!DOCTYPE html>
<html lang="en">
<head>
<meta charset="utf-8">
<title>Vantoria Pocket Folder</title>
<link rel="stylesheet" href="https://fonts.googleapis.com/css2?family=Roboto:wght@400;500&family=Tinos&display=swap">
<style>
  :root {
    --page: #ffffff;
    --outline: #6f6f6f;
    --panel-white: #f4f4f4;
    --slate: #707070;
    --sky-blue: #17b4e6;
    --logo-grey: #5c5d60;
    --tagline-grey: #6a6a6a;
    --band-text: #ffffff;
    --hatch: #b9b9b9;
  }
  html, body {
    margin: 0;
    width: 1200px;
    height: 675px;
    overflow: hidden;
    background: var(--page);
  }
  .folder-spread {
    position: absolute;
    left: 215px;
    top: 27px;
    width: 770px;
    height: 620px;
  }
  .outline { stroke: var(--outline); stroke-width: 1.2; fill: none; }
  .cover-white { fill: var(--panel-white); }
  .band-slate { fill: var(--slate); }
  .band-blue { fill: var(--sky-blue); }
  .glue-flap { fill: url(#glue-hatch); stroke: var(--outline); stroke-width: 1; }
  .card-slit { stroke: #3f3f3f; stroke-width: 1.4; fill: none; }
  .notch { fill: var(--page); stroke: var(--outline); stroke-width: 1; }
  .brand-name {
    font-family: "Roboto", Arial, sans-serif;
    font-weight: 500;
  }
  .brand-name--cover { fill: var(--logo-grey); font-size: 31px; }
  .brand-name--band { fill: var(--band-text); font-size: 12px; }
  .brand-square--cover { fill: var(--logo-grey); }
  .brand-square--band { fill: var(--band-text); }
  .tagline {
    font-family: "Tinos", "Times New Roman", serif;
    font-size: 8.5px;
  }
  .tagline--cover { fill: var(--tagline-grey); }
  .tagline--band { fill: var(--band-text); font-size: 7.5px; }
</style>
</head>
<body>
<svg class="folder-spread" viewBox="625 100 800 645" xmlns="http://www.w3.org/2000/svg">
  <defs>
    <pattern id="glue-hatch" width="6" height="6" patternUnits="userSpaceOnUse" patternTransform="rotate(45)">
      <rect width="6" height="6" fill="#ffffff"/>
      <line x1="0" y1="0" x2="0" y2="6" stroke="var(--hatch)" stroke-width="1.5"/>
    </pattern>
    <linearGradient id="skyline-road" x1="0" y1="0" x2="0" y2="1">
      <stop offset="0" stop-color="#cfe3f0"/>
      <stop offset="0.35" stop-color="#c9a98c"/>
      <stop offset="0.6" stop-color="#5f7f45"/>
      <stop offset="1" stop-color="#8d8aa0"/>
    </linearGradient>
    <linearGradient id="skyline-glass" x1="0" y1="0" x2="0" y2="1">
      <stop offset="0" stop-color="#3c8fd8"/>
      <stop offset="0.45" stop-color="#8fbfe6"/>
      <stop offset="1" stop-color="#33475c"/>
    </linearGradient>
  </defs>

  <!-- lower pockets -->
  <g class="pocket pocket--left">
    <rect class="glue-flap" x="663" y="568" width="27" height="170"/>
    <path class="band-slate" d="M690 565 H1026 L1002 728 Q1000 738 990 738 H690 Z"/>
    <path class="card-slit" d="M798 613 L774 637 M888 613 L912 637 M774 667 L798 691 M912 667 L888 691"/>
  </g>
  <g class="pocket pocket--right">
    <path class="band-blue" d="M1030 565 H1365 V738 H1066 Q1056 738 1054 728 Z"/>
    <rect class="glue-flap" x="1365" y="568" width="27" height="170"/>
    <g transform="rotate(180 1214 643)">
      <rect class="brand-square--band" x="1173" y="636" width="10" height="12"/>
      <text class="brand-name brand-name--band" x="1186" y="647">Vantoria</text>
    </g>
  </g>

  <!-- back cover -->
  <g class="cover cover--back">
    <rect x="632" y="105" width="396" height="385" fill="url(#skyline-road)" role="img" aria-label="Photo of the downtown skyline behind a tree-lined freeway"/>
    <path class="band-slate" d="M632 490 H1028 V565 H632 Q632 565 632 560 Z"/>
    <rect class="brand-square--band" x="793" y="509" width="9" height="12"/>
    <text class="brand-name brand-name--band" x="806" y="520">Vantoria</text>
    <text class="tagline tagline--band" x="848" y="538" text-anchor="middle">Group Insurance www.vantoriagroup-example.com</text>
  </g>

  <!-- front cover -->
  <g class="cover cover--front">
    <rect class="cover-white" x="1028" y="105" width="392" height="120"/>
    <rect class="brand-square--cover" x="1111" y="135" width="36" height="38"/>
    <text class="brand-name brand-name--cover" x="1157" y="167">Vantoria</text>
    <text class="tagline tagline--cover" x="1213" y="187" text-anchor="middle">Group Insurance www.vantoriagroup-example.com</text>
    <rect x="1028" y="225" width="392" height="265" fill="url(#skyline-glass)" role="img" aria-label="Photo looking up at glass office towers against a blue sky"/>
    <rect class="band-blue" x="1028" y="490" width="392" height="75"/>
  </g>

  <!-- die outline -->
  <path class="outline" d="M632 110 Q632 105 640 105 H1412 Q1420 105 1420 110 V560 Q1420 565 1410 568 H1392 V738 H1066 Q1056 738 1054 728 L1028 570 L1002 728 Q1000 738 990 738 H663 V568 H642 Q632 565 632 560 Z"/>
  <line class="outline" x1="1028" y1="105" x2="1028" y2="565"/>
  <path class="notch" d="M632 386 A9 9 0 0 1 632 404 Z"/>
  <path class="notch" d="M1420 386 A9 9 0 0 0 1420 404 Z"/>
</svg>
</body>
</html>
```